Business Card Design Project

double sided, embossed, name & logo on front font sonsie one, back Name Marisol Venkamp, mobile 0468201934, Phone 73519086,
email marisol@brightspanservices.com, use sysbols on the back for example an envelope for email, a telephone for phone number etc.symbol slate grey writing navy blue

Industry/Entity Type

Business

```html
<!DOCTYPE html>
<html lang="en">
<head>
<meta charset="utf-8">
<title>Brightspan Services – Business Card</title>
<link rel="stylesheet" href="https://fonts.googleapis.com/css2?family=Sonsie+One&family=PT+Serif&display=swap">
<style>
  :root {
    --page: #eef0f0;
    --periwinkle: #6670ff;
    --navy: #191f84;
    --white: #ffffff;
    --icon: #a8aedb;
    --shadow: rgba(60, 66, 70, 0.55);
  }
  * { margin: 0; padding: 0; box-sizing: border-box; }
  html, body {
    width: 1200px;
    height: 1200px;
    overflow: hidden;
    background: var(--page);
  }
  .canvas {
    position: relative;
    width: 1200px;
    height: 1200px;
  }
  .card {
    position: absolute;
    left: 144px;
    width: 890px;
    height: 494px;
    box-shadow: 8px 8px 6px var(--shadow);
    overflow: hidden;
  }
  /* Front */
  .card--front {
    top: 58px;
    background: var(--periwinkle);
  }
  .brand-name {
    position: absolute;
    left: 50px;
    right: 50px;
    top: 212px;
    text-align: center;
    font-family: "Sonsie One", cursive;
    font-size: 50px;
    font-weight: 400;
    line-height: 1;
    color: var(--navy);
    white-space: nowrap;
  }
  .band {
    position: absolute;
    left: 0;
    width: 100%;
  }
  .band--white { top: 332px; height: 34px; background: var(--white); }
  .band--navy { top: 366px; height: 35px; background: var(--navy); }

  /* Back */
  .card--back {
    top: 634px;
    background: var(--white);
  }
  .stripe {
    position: absolute;
    top: 0;
    height: 100%;
    width: 34px;
  }
  .stripe--navy { left: 36px; background: var(--navy); }
  .stripe--light { left: 70px; background: var(--periwinkle); }
  .person-name {
    position: absolute;
    left: 120px;
    top: 196px;
    font-family: "Sonsie One", cursive;
    font-size: 41px;
    font-weight: 400;
    line-height: 1;
    color: var(--periwinkle);
    white-space: nowrap;
  }
  .contact {
    position: absolute;
    display: flex;
    align-items: center;
    font-family: "PT Serif", serif;
    font-size: 19px;
    line-height: 26px;
    color: var(--navy);
    white-space: nowrap;
  }
  .contact--phone { left: 130px; top: 282px; }
  .contact--email { left: 468px; top: 293px; }
  .contact svg { flex: none; }
  .contact--phone svg { margin-right: 13px; }
  .contact--email svg { margin-right: 12px; }
</style>
</head>
<body>
<main class="canvas">
  <section class="card card--front" aria-label="Card front">
    <h1 class="brand-name">Brightspan Services</h1>
    <div class="band band--white"></div>
    <div class="band band--navy"></div>
  </section>

  <section class="card card--back" aria-label="Card back">
    <div class="stripe stripe--navy"></div>
    <div class="stripe stripe--light"></div>
    <h2 class="person-name">Marisol Venkamp</h2>

    <div class="contact contact--phone">
      <svg class="icon-phone" width="78" height="80" viewBox="0 0 78 80" fill="none" stroke="var(--icon)" stroke-width="2.4" stroke-linejoin="round" stroke-linecap="round" aria-hidden="true">
        <path d="M14 6 L24 4 L30 20 L22 26 Q26 42 38 52 L46 46 L58 58 L52 70 Q40 78 26 64 Q8 44 6 22 Q6 10 14 6 Z"/>
        <path d="M38 22 Q46 26 48 34"/>
        <path d="M40 12 Q54 18 58 32"/>
        <path d="M44 2 Q64 10 68 30"/>
      </svg>
      <div class="contact-lines">
        <div>Mobile: 0468201934</div>
        <div>Phone: 73519086</div>
      </div>
    </div>

    <div class="contact contact--email">
      <svg class="icon-mail" width="76" height="52" viewBox="0 0 76 52" fill="none" stroke="var(--icon)" stroke-width="2.4" stroke-linejoin="round" aria-hidden="true">
        <rect x="2" y="2" width="72" height="48"/>
        <path d="M2 2 L38 30 L74 2"/>
        <path d="M2 50 L30 24"/>
        <path d="M74 50 L46 24"/>
      </svg>
      <span>marisol@brightspanservices.com</span>
    </div>
  </section>
</main>
</body>
</html>
```